Calendar Design Project: 2025 with Specific Edits

This is a straightforward project where your creativity can shine!
Simply take the existing 2024 calendar and adapt it for 2025 by incorporating the new photos I've attached.
Please keep the overall concept of the 2024 calendar intact—your focus will be on enhancing it with fresh visuals.

I can't wait to see your amazing designs!
I am looking for a talented graphic designer to create a new 2025 calendar with specific adjustments.
Pictures attached.
Requirements:
Calendar Size: 52cm x 34cm
March Folder:
Adjust the image named "attached - DJI-0025" to make the circular road darker to match the rest of the design.
May Folder:
Modify the circled area in the May image to ensure it looks consistent with the other road (reference file: "attached - After").
November Folder:
Clear out the circled area in the November image (reference file: "attached - After1").
Please let me know if you have any questions or need further clarification.
I added to my breif a design i made last year for same client.
2025, calendar should be vertical and not horizontal. and some of the photos attache are "Before" and "After" please include together inside each month of the calendar.
Thank you!
Feel free to adjust any details as necessary!

Hello talented designers!

I’m excited to share that this is my 14th project on the ArtHarbor platform, and I’ve been fortunate to have successful collaborations in the past. I'm looking forward to creating a new 2025 calendar with your help, and I believe that with your creativity and skills, we can make this project a success as well!

I hope to establish a long-term relationship with a talented team like yours. As an added incentive, I will be offering a bonus for the winner, and I may select more than one winner, so everyone has a chance to shine!

Let’s make something amazing together!

Best
Update:
cancel or before, only place the After picture

Requirements
Must have
• Project Overview Objective: Create a 2025 calendar using the provided images, maintaining the design concept from the 2024 calendar but enhancing it with new visuals. Format: Vertical layout (52cm x 34cm).

```html
<!DOCTYPE html>
<html lang="en">
<head>
<meta charset="utf-8">
<title>Norvale Builders Ltd — Calendar 2025, December</title>
<link href="https://fonts.googleapis.com/css2?family=Open+Sans:wght@400;600&display=swap" rel="stylesheet">
<style>
  :root{
    --backdrop:#ecefec;
    --paper:#ffffff;
    --ink:#161616;
    --ink-soft:#5a5a5a;
    --lime:#8fe61c;
    --lime-text:#4fdc47;
    --lime-cell:#cbfbb5;
    --grey-cell:#f1f2f3;
  }
  *{box-sizing:border-box;margin:0;padding:0}
  html,body{width:1200px;height:848px;overflow:hidden}
  body{background:var(--backdrop);font-family:"Open Sans",sans-serif;color:var(--ink);position:relative}

  .calendar-page{position:absolute;left:332px;top:14px;width:536px;height:820px;background:var(--paper);overflow:hidden}
  .page-art{position:absolute;left:0;top:0;width:536px;height:440px}

  .brand{position:absolute;left:47px;top:44px;display:flex;align-items:center;gap:8px}
  .brand-mark{width:14px;height:14px;background:var(--ink);flex:none}
  .brand-name{font-weight:600;font-size:17px;line-height:1.05;color:var(--ink);letter-spacing:.5px}

  .title-block{position:absolute;left:26px;top:434px}
  .title-label{font-size:22px;color:var(--lime-text);line-height:1}
  .title-year{font-size:51px;line-height:1;margin-top:-2px;letter-spacing:1px}
  .month-name{position:absolute;left:229px;top:478px;font-size:30px;color:var(--ink-soft);letter-spacing:.5px;line-height:1}

  .month-grid{position:absolute;left:26px;top:528px;display:grid;grid-template-columns:repeat(7,48.4px);column-gap:3px}
  .weekday{height:28px;display:flex;align-items:center;justify-content:center;font-size:7px;font-weight:600;background:var(--grey-cell);margin-bottom:6px;white-space:nowrap}
  .day{height:34px;margin-bottom:9.4px;background:var(--grey-cell);font-size:19px;line-height:1;display:flex;align-items:flex-end;padding:0 0 1px 6px}
  .weekend{background:var(--lime-cell)}

  .mini-month{position:absolute;left:391px;width:122px}
  .mini-november{top:523px}
  .mini-january{top:674px}
  .mini-title{font-size:7.5px;color:var(--ink-soft);margin-bottom:3px;white-space:nowrap}
  .mini-title .mini-year{color:var(--lime-text)}
  .mini-grid{display:grid;grid-template-columns:repeat(7,15.6px);column-gap:1.8px}
  .mini-weekday{height:7px;font-size:2.6px;display:flex;align-items:center;justify-content:center;background:var(--grey-cell);margin-bottom:4px;overflow:hidden;white-space:nowrap}
  .mini-day{height:9.6px;margin-bottom:5px;font-size:6px;display:flex;align-items:center;padding-left:2px;background:var(--paper)}
  .mini-grid .weekend{background:var(--lime-cell)}
  .mini-day.blank{background:var(--grey-cell)}

  .page-footer{position:absolute;left:26px;top:788px;right:20px;display:flex;align-items:center;gap:9px;font-size:5.4px;color:var(--ink-soft);white-space:nowrap}
  .footer-brand{display:flex;align-items:center;gap:3px;font-weight:600;font-size:6.5px;color:var(--ink);margin-right:8px}
  .footer-brand .brand-mark{width:6px;height:6px}
  .footer-key{color:var(--lime-text);font-weight:600}
</style>
</head>
<body>
<main class="calendar-page">
  <svg class="page-art" viewBox="0 0 536 440" xmlns="http://www.w3.org/2000/svg">
    <defs>
      <linearGradient id="wave-top" x1="0" y1="0" x2="1" y2="0">
        <stop offset="0" stop-color="#d9f6b4"/><stop offset=".5" stop-color="#f6fdea"/><stop offset="1" stop-color="#9ae82a"/>
      </linearGradient>
      <linearGradient id="wave-bottom" x1="0" y1="0" x2="1" y2="0">
        <stop offset="0" stop-color="#ffffff"/><stop offset=".45" stop-color="#c4f27a"/><stop offset="1" stop-color="#8fe61c"/>
      </linearGradient>
      <linearGradient id="photo-tone" x1="0" y1="0" x2="1" y2="1">
        <stop offset="0" stop-color="#d3d0cb"/><stop offset="1" stop-color="#bdb6ae"/>
      </linearGradient>
    </defs>
    <path d="M0,0 H536 V59 C420,50 300,70 200,110 C120,140 50,132 0,115 Z" fill="url(#wave-top)"/>
    <path role="img" aria-label="Photo of the company's fleet of construction trucks parked on a site" d="M0,115 C50,132 120,140 200,110 C300,70 420,50 536,59 V308 C430,350 300,368 200,358 C120,352 50,344 0,361 Z" fill="url(#photo-tone)"/>
    <path d="M0,361 C50,344 120,352 200,358 C300,368 430,350 536,308 V431 C430,445 330,425 250,400 C160,372 80,380 0,372 Z" fill="url(#wave-bottom)"/>
  </svg>

  <div class="brand">
    <span class="brand-mark"></span>
    <span class="brand-name">NORVALE<br>BUILDERS LTD</span>
  </div>

  <div class="title-block">
    <p class="title-label">CALENDAR</p>
    <p class="title-year">2025</p>
  </div>
  <p class="month-name">DECEMBER</p>

  <section class="month-grid">
    <div class="weekday weekend">SUNDAY</div><div class="weekday">MONDAY</div><div class="weekday">TUESDAY</div><div class="weekday">WEDNESDAY</div><div class="weekday">THURSDAY</div><div class="weekday">FRIDAY</div><div class="weekday weekend">SATURDAY</div>
    <div class="day weekend"></div><div class="day">1</div><div class="day">2</div><div class="day">3</div><div class="day">4</div><div class="day">5</div><div class="day weekend">6</div>
    <div class="day weekend">7</div><div class="day">8</div><div class="day">9</div><div class="day">10</div><div class="day">11</div><div class="day">12</div><div class="day weekend">13</div>
    <div class="day weekend">14</div><div class="day">15</div><div class="day">16</div><div class="day">17</div><div class="day">18</div><div class="day">19</div><div class="day weekend">20</div>
    <div class="day weekend">21</div><div class="day">22</div><div class="day">23</div><div class="day">24</div><div class="day">25</div><div class="day">26</div><div class="day weekend">27</div>
    <div class="day weekend">28</div><div class="day">29</div><div class="day">30</div><div class="day">31</div><div class="day"></div><div class="day"></div><div class="day weekend"></div>
  </section>

  <section class="mini-month mini-november">
    <p class="mini-title">NOVEMBER &nbsp;| &nbsp;<span class="mini-year">2025</span></p>
    <div class="mini-grid">
      <div class="mini-weekday weekend">SUNDAY</div><div class="mini-weekday">MONDAY</div><div class="mini-weekday">TUESDAY</div><div class="mini-weekday">WEDNESDAY</div><div class="mini-weekday">THURSDAY</div><div class="mini-weekday">FRIDAY</div><div class="mini-weekday weekend">SATURDAY</div>
      <div class="mini-day weekend">30</div><div class="mini-day blank"></div><div class="mini-day blank"></div><div class="mini-day blank"></div><div class="mini-day blank"></div><div class="mini-day blank"></div><div class="mini-day weekend">1</div>
      <div class="mini-day weekend">2</div><div class="mini-day">3</div><div class="mini-day">4</div><div class="mini-day">5</div><div class="mini-day">6</div><div class="mini-day">7</div><div class="mini-day weekend">8</div>
      <div class="mini-day weekend">9</div><div class="mini-day">10</div><div class="mini-day">11</div><div class="mini-day">12</div><div class="mini-day">13</div><div class="mini-day">14</div><div class="mini-day weekend">15</div>
      <div class="mini-day weekend">16</div><div class="mini-day">17</div><div class="mini-day">18</div><div class="mini-day">19</div><div class="mini-day">20</div><div class="mini-day">21</div><div class="mini-day weekend">22</div>
      <div class="mini-day weekend">23</div><div class="mini-day">24</div><div class="mini-day">25</div><div class="mini-day">26</div><div class="mini-day">27</div><div class="mini-day">28</div><div class="mini-day weekend">29</div>
    </div>
  </section>

  <section class="mini-month mini-january">
    <p class="mini-title">JANUARY &nbsp;| &nbsp;<span class="mini-year">2026</span></p>
    <div class="mini-grid">
      <div class="mini-weekday weekend">SUNDAY</div><div class="mini-weekday">MONDAY</div><div class="mini-weekday">TUESDAY</div><div class="mini-weekday">WEDNESDAY</div><div class="mini-weekday">THURSDAY</div><div class="mini-weekday">FRIDAY</div><div class="mini-weekday weekend">SATURDAY</div>
      <div class="mini-day weekend"></div><div class="mini-day blank"></div><div class="mini-day blank"></div><div class="mini-day blank"></div><div class="mini-day">1</div><div class="mini-day">2</div><div class="mini-day weekend">3</div>
      <div class="mini-day weekend">4</div><div class="mini-day">5</div><div class="mini-day">6</div><div class="mini-day">7</div><div class="mini-day">8</div><div class="mini-day">9</div><div class="mini-day weekend">10</div>
      <div class="mini-day weekend">11</div><div class="mini-day">12</div><div class="mini-day">13</div><div class="mini-day">14</div><div class="mini-day">15</div><div class="mini-day">16</div><div class="mini-day weekend">17</div>
      <div class="mini-day weekend">18</div><div class="mini-day">19</div><div class="mini-day">20</div><div class="mini-day">21</div><div class="mini-day">22</div><div class="mini-day">23</div><div class="mini-day weekend">24</div>
      <div class="mini-day weekend">25</div><div class="mini-day">26</div><div class="mini-day">27</div><div class="mini-day">28</div><div class="mini-day">29</div><div class="mini-day">30</div><div class="mini-day weekend">31</div>
    </div>
  </section>

  <footer class="page-footer">
    <span class="footer-brand"><span class="brand-mark"></span>NORVALE BUILDERS LTD</span>
    <span><span class="footer-key">T:</span> +2348005550142</span>
    <span><span class="footer-key">E:</span> hello@norvalebuilders.com</span>
    <span><span class="footer-key">W:</span> www.norvalebuilders.com</span>
    <span><span class="footer-key">A:</span> Palmgrove Street, Off Harbor Crescent, Eastline, Lakeview</span>
  </footer>
</main>
</body>
</html>
```